Entrepreneur needs a business card design

I need a business card to name my three companies, as well as contact information.
I'm open on design and color and it can be plain or complex. I'm open on colors but I think I prefer something somewhat formal but fun as well.
I'm open on whether the background is plain or has design in it. I don't have company logos.
Target Market(s)
Auto dealers, realtors and property managers
Industry/Entity Type
Business
Contact Information for Business Card
HOLLISTER FAMILY PROPERTIES, LLC
HOLLISTER PUBLISHING, LLC
LOTMASTER CONSULTING, LLC
Ned Hollister
2847 W. Tamarack Ave. #310
Boise, Idaho 83611-2905
208-514-3092
ned@holl5x.example

```html
<!DOCTYPE html>
<html lang="en">
<head>
<meta charset="utf-8">
<title>Ned Varrow — Business Card</title>
<link href="https://fonts.googleapis.com/css2?family=Roboto+Condensed:wght@300;700&display=swap" rel="stylesheet">
<style>
  :root {
    --page: #eceef1;
    --sky: #0a8fd8;
    --sky-mid: #35a9e2;
    --paper: #ffffff;
    --band: #0c4d9f;
    --band-text: #ffffff;
    --name: #0b4a9c;
    --contact: #4d7fc6;
  }
  html, body {
    margin: 0;
    width: 1200px;
    height: 1000px;
    overflow: hidden;
    background: var(--page);
  }
  .card {
    position: absolute;
    left: 75px;
    top: 200px;
    width: 1050px;
    height: 600px;
    border-radius: 26px;
    overflow: hidden;
    background: linear-gradient(200deg, var(--sky) 0%, var(--sky-mid) 38%, var(--paper) 74%);
    box-shadow: 0 14px 40px rgba(0, 0, 0, 0.18);
  }
  .card-art {
    position: absolute;
    inset: 0;
  }
  .company-band { fill: var(--band); }
  .swoosh { fill: var(--paper); }
  .company-name {
    font-family: "Roboto Condensed", "Arial Narrow", sans-serif;
    font-weight: 700;
    font-size: 40px;
    fill: var(--band-text);
    letter-spacing: 0.5px;
  }
  .contact {
    position: absolute;
    right: 70px;
    top: 400px;
    text-align: right;
    font-family: "Roboto Condensed", "Arial Narrow", sans-serif;
  }
  .contact-name {
    margin: 0 0 6px;
    font-weight: 700;
    font-size: 46px;
    color: var(--name);
    line-height: 1.1;
  }
  .contact-line {
    margin: 0;
    font-weight: 300;
    font-size: 32px;
    color: var(--contact);
    line-height: 1.3;
  }
  .contact-line .gap { display: inline-block; width: 14px; }
</style>
</head>
<body>
  <div class="card">
    <svg class="card-art" width="1050" height="600" viewBox="0 0 1050 600" aria-hidden="true">
      <defs>
        <path id="line-properties" d="M350,118 Q640,150 960,182"/>
        <path id="line-publishing" d="M250,190 Q560,228 920,262"/>
        <path id="line-consulting" d="M155,262 Q480,305 880,342"/>
      </defs>

      <path class="company-band" d="M330,72 Q640,104 1000,138 L985,200 Q640,170 320,134 Z"/>
      <path class="company-band" d="M230,144 Q560,180 960,218 L945,280 Q560,246 220,206 Z"/>
      <path class="company-band" d="M130,216 Q480,258 920,298 L905,360 Q480,322 120,278 Z"/>

      <path class="swoosh" d="M700,384 Q880,340 1040,292 Q880,346 704,390 Z"/>

      <text class="company-name"><textPath href="#line-properties">Varrow Family Properties, LLC</textPath></text>
      <text class="company-name"><textPath href="#line-publishing">Varrow Publishing, LLC</textPath></text>
      <text class="company-name"><textPath href="#line-consulting">Lotmaster Consulting, LLC</textPath></text>
    </svg>

    <div class="contact">
      <p class="contact-name">Ned Varrow</p>
      <p class="contact-line">2847 W. Tamarack Ave. #310 Boise, Idaho 83611-2905</p>
      <p class="contact-line">208-514-3092<span class="gap"></span>ned@varr5x.example</p>
    </div>
  </div>
</body>
</html>
```